real esate business card with company logo and name

we need a business card design for a real esate company

The company name is Walsh & Ortiz Pty Ltd, and we have our logo designed and will upload. We want classic or moden feel. Black or white background. looks more textured. Should include folowinginformations
Paul Walsh and Tara Ortiz
Sales Agents & Onsite Manager
p: 07 5948 2610
F: 07 5948 2795
M:0451 786 923
3/22 Marlow Crescent, ASHWOOD VALE QLD 4093

We want this business card looks professonal. Thank you in advance.

Industry/Entity Type

Real Estate Agent

Contact Information for Business Card

Paul Walsh and Tara Ortiz
Onsite Manager & Sales Agents
p: 07 5948 2610
M:0451 786 923

Font styles to use
Serif

Colors
000000
fbfbfb
333333
959595

Requirements
Must have
• company logo and name, black or white back ground

```html
<!DOCTYPE html>
<html lang="en">
<head>
<meta charset="utf-8">
<title>Walsh &amp; Ortiz Pty Ltd – Business Card</title>
<link href="https://fonts.googleapis.com/css2?family=Lato:wght@400;700;900&display=swap" rel="stylesheet">
<style>
  :root {
    --backdrop: #dcdcdc;
    --card: #fbfbfb;
    --band-top: #a5a5a7;
    --band-bottom: #636467;
    --rule-light: #9a9a9c;
    --rule-dark: #6e6f72;
    --ink: #5e5f62;
    --ink-soft: #8d8e90;
    --icon: #6a6b6e;
  }
  * { margin: 0; padding: 0; box-sizing: border-box; }
  html, body {
    width: 1200px; height: 800px; overflow: hidden;
    background: var(--backdrop);
    font-family: "Lato", sans-serif;
  }
  .card {
    position: absolute; left: 100px; top: 100px;
    width: 1000px; height: 600px;
    background: var(--card);
    box-shadow: 0 6px 18px rgba(0,0,0,.18);
    overflow: hidden;
  }
  .band-top { position: absolute; left: 0; top: 0; width: 100%; height: 78px; background: var(--band-top); }
  .band-bottom { position: absolute; left: 0; bottom: 0; width: 100%; height: 112px; background: var(--band-bottom); }

  .company { position: absolute; left: 54px; top: 142px; color: var(--ink); }
  .company-name { font-weight: 900; font-size: 34px; letter-spacing: 1px; line-height: 1; }
  .company-suffix { font-size: 17px; letter-spacing: 1px; color: var(--ink-soft); margin-top: 2px; padding-left: 4px; }

  .agents { position: absolute; right: 84px; top: 102px; text-align: right; color: var(--ink); }
  .agents-names { font-weight: 900; font-size: 31px; letter-spacing: .3px; line-height: 1; }
  .agents-role { font-size: 17px; color: var(--ink-soft); letter-spacing: .6px; margin-top: 3px; }

  .rule { position: absolute; height: 6px; }
  .rule-left { left: 0; top: 232px; width: 690px; background: var(--rule-light); }
  .rule-right { left: 702px; top: 194px; width: 298px; background: var(--rule-dark); }

  .contacts { position: absolute; left: 66px; top: 300px; list-style: none; }
  .contacts li { display: flex; align-items: center; height: 38px; font-size: 21px; color: var(--ink); letter-spacing: .8px; white-space: nowrap; }
  .contacts svg { width: 24px; height: 24px; margin-right: 24px; fill: var(--icon); flex: none; }

  .brand { position: absolute; left: 760px; top: 290px; width: 200px; display: flex; flex-direction: column; align-items: center; gap: 14px; }
  .brand-square { width: 46px; height: 46px; background: var(--rule-dark); }
  .brand-name { font-weight: 900; font-size: 26px; color: var(--ink); letter-spacing: .5px; white-space: nowrap; }
</style>
</head>
<body>
  <section class="card">
    <div class="band-top"></div>

    <div class="company">
      <div class="company-name">WALSH &amp; ORTIZ</div>
      <div class="company-suffix">PTY LTD</div>
    </div>

    <div class="agents">
      <div class="agents-names">PAUL WALSH AND TARA ORTIZ</div>
      <div class="agents-role">Onsite Manager &amp; Sales Agents</div>
    </div>

    <div class="rule rule-left"></div>
    <div class="rule rule-right"></div>

    <ul class="contacts">
      <li>
        <svg viewBox="0 0 24 24" aria-hidden="true"><path d="M2 9c0-3 4.5-5 10-5s10 2 10 5v2h-5V9c-1.5-.7-3.2-1-5-1s-3.5.3-5 1v2H2z"/><path d="M5 13h14l2 7H3z"/><circle cx="12" cy="16" r="2" fill="#fbfbfb"/></svg>
        07 5948 2610
      </li>
      <li>
        <svg viewBox="0 0 24 24" aria-hidden="true"><path d="M7 2h10a2 2 0 0 1 2 2v16a2 2 0 0 1-2 2H7a2 2 0 0 1-2-2V4a2 2 0 0 1 2-2zm0 3v13h10V5z"/><circle cx="12" cy="20" r="1" fill="#fbfbfb"/></svg>
        0451 786 923
      </li>
      <li>
        <svg viewBox="0 0 24 24" aria-hidden="true"><rect x="1" y="8" width="5" height="14"/><path d="M8 2h10v6h4v14H8z"/><rect x="10" y="4" width="6" height="4" fill="#fbfbfb"/><g fill="#fbfbfb"><rect x="11" y="11" width="2" height="2"/><rect x="15" y="11" width="2" height="2"/><rect x="11" y="15" width="2" height="2"/><rect x="15" y="15" width="2" height="2"/><rect x="11" y="19" width="2" height="1.5"/><rect x="15" y="19" width="2" height="1.5"/></g></svg>
        07 5948 2795
      </li>
      <li>
        <svg viewBox="0 0 24 24" aria-hidden="true"><path d="M12 1a8 8 0 0 0-8 8c0 6 8 14 8 14s8-8 8-14a8 8 0 0 0-8-8zm0 11a3 3 0 1 1 0-6 3 3 0 0 1 0 6z"/></svg>
        3/22 Marlow Crescent, ASHWOOD VALE QLD 4093
      </li>
    </ul>

    <div class="brand">
      <div class="brand-square"></div>
      <div class="brand-name">Walsh &amp; Ortiz</div>
    </div>

    <div class="band-bottom"></div>
  </section>
</body>
</html>
```